Book Cover design for book about character and ethics

This is an exciting book about what it means to live an authentic life. It revolves around finding a sense of contentment, solid friendships and being a good person. The idea is to move away from chasing excessive wealth, good looks and popularity in order to find happiness. Authentic happiness requires a different chase. This book is also about a solid foundation, priorities and work / life balance.

I want a cover that is CREATIVE and POPS. It needs to stand out on the shelf from other books.

Target Market(s)

High school, college and working professionals.

Font styles to use
Serif

Requirements
Must have
• Title: True Otters: Seek A Grounded Path
• Author Name: Dana Velmoravi
• Creativity - makes the point without being entirely obvious
• Cover must pop in comparison to other books
• Use bright colors
• Easy to read text
• Cool picture or vector art
Nice to have
• Topics to think about:
• 1. Stand out from the crowd
• 2. The world is lying to you about what makes you happy
• 3. Renewal
• 4. Rebuild
• 5. Chase What Matters
• 6. Pushing against the wind
• I included some pics below as guidance
Should not have
• Cannot be cheesy
• Do not put a rabbit on the cover even though the book is called "True Otters"

```html
<!DOCTYPE html>
<html lang="en">
<head>
<meta charset="utf-8">
<title>True Otters: Seek A Grounded Path — Book Cover</title>
<link rel="stylesheet" href="https://fonts.googleapis.com/css2?family=Alfa+Slab+One&display=swap">
<style>
  :root {
    --backdrop: #ffffff;
    --cover-light: #efefed;
    --cover-mid: #d6d6d2;
    --cover-edge: #bcbcb7;
    --ink: #2b2b2a;
    --accent: #e0743a;
    --accent-deep: #cf4d1f;
    --herd: #1f1f1f;
    --herd-soft: #3a3a39;
  }
  html, body {
    margin: 0;
    padding: 0;
    width: 1200px;
    height: 1200px;
    overflow: hidden;
    background: var(--backdrop);
  }
  .canvas {
    width: 1200px;
    height: 1200px;
    display: flex;
    align-items: center;
    justify-content: center;
  }
  .book-cover {
    position: relative;
    width: 730px;
    height: 1110px;
    background: radial-gradient(ellipse 62% 48% at 50% 52%, var(--cover-light) 0%, var(--cover-mid) 68%, var(--cover-edge) 100%);
    overflow: hidden;
  }
  .cover-title {
    position: absolute;
    top: 98px;
    left: 0;
    right: 0;
    margin: 0;
    text-align: center;
    color: var(--ink);
    font-family: "Alfa Slab One", "Rockwell", serif;
    font-weight: 400;
    line-height: 1;
  }
  .cover-title .title-main {
    display: block;
    font-size: 82px;
    letter-spacing: 1px;
    white-space: nowrap;
  }
  .cover-title .title-sub {
    display: block;
    margin-top: 12px;
    font-size: 46px;
    letter-spacing: 0.5px;
    white-space: nowrap;
  }
  .cover-title .title-highlight {
    color: var(--accent);
  }
  .cover-art {
    position: absolute;
    left: 50%;
    top: 335px;
    width: 495px;
    height: 505px;
    transform: translateX(-50%);
  }
  .cover-author {
    position: absolute;
    bottom: 72px;
    left: 0;
    right: 0;
    margin: 0;
    text-align: center;
    color: var(--ink);
    font-family: "Alfa Slab One", "Rockwell", serif;
    font-weight: 400;
    font-size: 27px;
    letter-spacing: 1px;
  }
</style>
</head>
<body>
  <main class="canvas">
    <article class="book-cover">
      <h1 class="cover-title">
        <span class="title-main">TRUE OTTERS</span>
        <span class="title-sub">SEEK A <span class="title-highlight">GROUNDED</span> PATH</span>
      </h1>

      <svg class="cover-art" viewBox="0 0 495 505" role="img"
           aria-label="Illustration: a diamond-shaped crowd of black animal silhouettes with a single orange one standing out at the centre">
        <defs>
          <radialGradient id="herd-tone" cx="50%" cy="50%" r="50%">
            <stop offset="0%" stop-color="var(--accent-deep)"/>
            <stop offset="9%" stop-color="var(--accent-deep)"/>
            <stop offset="20%" stop-color="var(--herd-soft)"/>
            <stop offset="100%" stop-color="var(--herd)"/>
          </radialGradient>
        </defs>
        <polygon points="247.5,0 495,252.5 247.5,505 0,252.5" fill="url(#herd-tone)"/>
      </svg>

      <p class="cover-author">Dana Velmoravi</p>
    </article>
  </main>
</body>
</html>
```